Mortgage Broking boutique Business

I’m wanting a revamped look to my existing business card design. I do like the black and silver but happy to have other colours introduced based on your creation. I’ve attached a copy of my current card so you can have a starting point updated details noted brloe. I deal with high net worth individuals so need my card to be sophisticated, classy that gives off a classy vibe

Target Market(s)

High net worth, wealthy

Industry/Entity Type

Mortgage Brokerage

Contact Information for Business Card

Job title: Finance Executive
Phone: +61 7 3287 4419
Mobile: 0471 352 608
Email: marcus@quillbrookcapital.com.au
Web: www.quillbrookcapital.com.au
Address: level 36 Tindale Court, 58 Harwick St Brisbane QLD 4000

Font styles to use
Other font styles liked:
• Helvetica

Colors

Designer to choose colors to be used in the design.

Requirements
Must have
• Use my existing card design as a starting point

```html
<!DOCTYPE html>
<html lang="en">
<head>
<meta charset="utf-8">
<title>Quillbrook Capital – Business Card</title>
<link href="https://fonts.googleapis.com/css2?family=Arimo:wght@400;700&display=swap" rel="stylesheet">
<style>
  :root {
    --backdrop: #b9c0c0;
    --card-black: #15171b;
    --card-black-soft: #1d2026;
    --strip-blue: #1f2733;
    --icon-tile: #2a323e;
    --paper: #e9e9e7;
    --ink: #111111;
    --silver: #d4d6d8;
    --silver-rule: #9ea2a6;
  }
  * { margin: 0; padding: 0; box-sizing: border-box; }
  html, body {
    width: 1200px; height: 720px; overflow: hidden;
    background: var(--backdrop);
    font-family: "Arimo", "Helvetica Neue", Helvetica, Arial, sans-serif;
  }
  .canvas {
    position: relative; width: 1200px; height: 720px;
    background: radial-gradient(ellipse at 35% 30%, #c9cfcf 0%, var(--backdrop) 60%, #a7afaf 100%);
  }
  .card {
    position: absolute; top: 205px; width: 540px; height: 310px;
    overflow: hidden;
    box-shadow: 0 14px 30px rgba(0,0,0,0.28);
  }
  .card--front { left: 40px; background: var(--paper); }
  .card--back { left: 620px; background: linear-gradient(170deg, var(--card-black-soft), var(--card-black)); }

  /* front */
  .brand-panel {
    position: absolute; left: 0; top: 0; width: 200px; height: 100%;
    background: var(--card-black);
    display: flex; flex-direction: column; align-items: center; justify-content: center;
  }
  .brand-name {
    color: var(--silver); font-weight: 400; text-align: center; line-height: 1;
  }
  .brand-panel .brand-name__main { font-size: 24px; letter-spacing: 2.5px; }
  .brand-panel .brand-name__sub { font-size: 11px; letter-spacing: 6px; margin-top: 8px; padding-left: 6px; }

  .icon-strip {
    position: absolute; left: 200px; top: 0; width: 38px; height: 100%;
    background: linear-gradient(90deg, #18202a, var(--strip-blue) 50%, #18202a);
  }
  .icon-tile {
    position: absolute; left: 7px; width: 24px; height: 24px;
    background: var(--icon-tile);
    display: flex; align-items: center; justify-content: center;
  }
  .icon-tile svg { width: 13px; height: 13px; fill: none; stroke: #c9ced6; stroke-width: 1.6; stroke-linecap: round; stroke-linejoin: round; }

  .details {
    position: absolute; left: 238px; top: 0; right: 0; height: 100%;
    color: var(--ink);
  }
  .job-title {
    position: absolute; top: 62px; left: 0; right: 0;
    text-align: center; font-weight: 700; font-size: 19px;
  }
  .contact-line {
    position: absolute; left: 22px; font-size: 14px; line-height: 18px; white-space: nowrap;
  }

  /* back */
  .back-rule {
    position: absolute; left: 0; right: 0; top: 188px; height: 2px;
    background: linear-gradient(90deg, var(--silver-rule), var(--silver), var(--silver-rule));
  }
  .back-brand {
    position: absolute; left: 0; right: 0; top: 100px; text-align: center;
  }
  .back-brand .brand-name__main { font-size: 40px; letter-spacing: 4px; }
  .back-brand .brand-name__sub { font-size: 15px; letter-spacing: 9px; margin-top: 10px; padding-left: 9px; }
</style>
</head>
<body>
<div class="canvas">

  <section class="card card--front" aria-label="Business card front">
    <div class="brand-panel">
      <div class="brand-name brand-name__main">QUILLBROOK</div>
      <div class="brand-name brand-name__sub">CAPITAL</div>
    </div>

    <div class="icon-strip">
      <div class="icon-tile" style="top:117px">
        <svg viewBox="0 0 16 16" aria-hidden="true"><path d="M4 2l2.5 3-1.5 1.5a8 8 0 004.5 4.5L11 9.5l3 2.5-1.5 2A10 10 0 012 3.5z"/></svg>
      </div>
      <div class="icon-tile" style="top:149px">
        <svg viewBox="0 0 16 16" aria-hidden="true"><rect x="4.5" y="1.5" width="7" height="13" rx="1.2"/><path d="M7 12.5h2"/></svg>
      </div>
      <div class="icon-tile" style="top:181px">
        <svg viewBox="0 0 16 16" aria-hidden="true"><circle cx="8" cy="8" r="6"/><path d="M2 8h12M8 2c2 2 2 10 0 12M8 2c-2 2-2 10 0 12"/></svg>
      </div>
      <div class="icon-tile" style="top:213px">
        <svg viewBox="0 0 16 16" aria-hidden="true"><rect x="2" y="4" width="12" height="8"/><path d="M2 4l6 5 6-5"/></svg>
      </div>
      <div class="icon-tile" style="top:245px">
        <svg viewBox="0 0 16 16" aria-hidden="true"><path d="M8 14.5s-4.5-5-4.5-8a4.5 4.5 0 019 0c0 3-4.5 8-4.5 8z"/><circle cx="8" cy="6.5" r="1.6"/></svg>
      </div>
    </div>

    <div class="details">
      <h1 class="job-title">Finance Executive</h1>
      <p class="contact-line" style="top:120px">+61 7 3287 4419</p>
      <p class="contact-line" style="top:152px">0471 352 608</p>
      <p class="contact-line" style="top:184px">www.quillbrookcapital.com.au</p>
      <p class="contact-line" style="top:216px">marcus@quillbrookcapital.com.au</p>
      <p class="contact-line" style="top:246px">level 36 Tindale Court, 58 Harwick<br>St Brisbane QLD 4000</p>
    </div>
  </section>

  <section class="card card--back" aria-label="Business card back">
    <div class="back-brand">
      <div class="brand-name brand-name__main">QUILLBROOK</div>
      <div class="brand-name brand-name__sub">CAPITAL</div>
    </div>
    <div class="back-rule"></div>
  </section>

</div>
</body>
</html>
```